Label Sticker for Tea Bag and Herbs and Spices Bag

I want to design the product label sticker size in 60 mm (H) x 100 mm (W).
This label is for our product herbal tea bag. We sell herbs such as Rose buds, Lavender, Chamomile, etc they are consider flower tea. Our products are natural dry herbs and spices.
I select Green, Brown, white as color combination. I can accept other colour proposed. If it look nice. However, only maximum 3 colours to play around and white is a compulsory colour.
I will print the product name, description, expiry date and instruction how to use and company name and address on it in black ink.
Prefer the label have natural look.
I would like to place my company logo in the label. Attached is the full colour artwork logo file.
I can accept one colour for logo since I only use 3 maximum colour.

Please advise the best design.

Reason: I am sorry as first time use Maple forum, I am not sure how to use the system.

Target Market(s)

To consumer who drink tea

Industry/Entity Type

It Company

Font styles to use
Serif

Requirements
Must have
• 60 mm (H) x 100 mm (w)
• Maximum 3 colour to play.
• Natural look and attraction to consumers.
Nice to have
• -Some drawing such as flower or leaves, lines, waves... as wallpaper
• -Can use 3 colour to separate Products name, Description and How to use.
• -Can give different colour besides my request for comparison.
• -Nice frame
Should not have
• Big pictures - Because it take the spaces, I cannot write more information in the label
• Too dark colour -Consumer cannot see the product information very clearly
• Too big logo - As it will take the space of the label.

```html
<!DOCTYPE html>
<html lang="en">
<head>
<meta charset="utf-8">
<title>Leafwell Moisturizer Label</title>
<link rel="stylesheet" href="https://fonts.googleapis.com/css2?family=Didact+Gothic&family=Pinyon+Script&family=Arimo:wght@700&display=swap">
<style>
  :root {
    --paper: #ffffff;
    --wallpaper: #fbf2ea;
    --brown: #8b3a2f;
    --tan: #b07a4f;
    --green: #a9b43a;
    --gold: #c8944a;
    --ink: #161616;
    --flourish: rgba(20, 20, 20, 0.16);
  }
  * { margin: 0; padding: 0; box-sizing: border-box; }
  html, body {
    width: 1200px;
    height: 721px;
    overflow: hidden;
    background: var(--paper);
  }
  .label {
    position: relative;
    width: 1200px;
    height: 721px;
    background: var(--paper);
  }
  .label__wallpaper {
    position: absolute;
    left: 56px;
    top: 47px;
    width: 1080px;
    height: 647px;
    border-radius: 48px;
    background: radial-gradient(ellipse at center, var(--paper) 35%, var(--wallpaper) 100%);
  }
  .label__frame {
    position: absolute;
    inset: 0;
  }
  .flourish {
    position: absolute;
    background: linear-gradient(135deg, var(--flourish), rgba(20, 20, 20, 0));
    border-radius: 6px;
  }
  .flourish--left { left: 60px; top: 54px; width: 108px; height: 118px; }
  .flourish--right {
    left: 1030px; top: 54px; width: 104px; height: 330px;
    background: linear-gradient(225deg, var(--flourish), rgba(20, 20, 20, 0) 70%);
  }
  .brand {
    position: absolute;
    left: 471px;
    top: 16px;
    width: 258px;
    height: 156px;
    display: flex;
    align-items: center;
    justify-content: center;
  }
  .brand__name {
    font-family: "Didact Gothic", sans-serif;
    font-size: 38px;
    letter-spacing: 3px;
    color: var(--brown);
  }
  .product-name {
    position: absolute;
    top: 202px;
    left: 0;
    width: 1200px;
    display: flex;
    justify-content: center;
    align-items: center;
    gap: 28px;
    font-family: "Pinyon Script", cursive;
    font-size: 46px;
    color: var(--tan);
  }
  .product-name__dot {
    width: 9px;
    height: 9px;
    border-radius: 50%;
    background: var(--brown);
  }
  .description {
    position: absolute;
    left: 300px;
    top: 296px;
    width: 600px;
    text-align: center;
    font-family: "Didact Gothic", sans-serif;
    font-size: 21px;
    line-height: 27.5px;
    letter-spacing: 1.2px;
    color: var(--ink);
  }
  .usage__title {
    position: absolute;
    top: 554px;
    left: 0;
    width: 1200px;
    text-align: center;
    font-family: "Pinyon Script", cursive;
    font-size: 33px;
    color: var(--brown);
  }
  .usage__text {
    position: absolute;
    left: 420px;
    top: 603px;
    width: 360px;
    text-align: center;
    font-family: "Arimo", sans-serif;
    font-weight: 700;
    font-size: 12.4px;
    line-height: 15.6px;
    color: var(--ink);
  }
</style>
</head>
<body>
  <main class="label">
    <div class="label__wallpaper" role="img" aria-label="Faint scattered leaf and petal wallpaper pattern"></div>

    <svg class="label__frame" width="1200" height="721" viewBox="0 0 1200 721" aria-hidden="true">
      <rect x="54" y="44" width="1085" height="653" rx="50" fill="none" stroke="var(--brown)" stroke-width="3"/>
      <polyline points="84,541 84,74 1120,74 1120,541" fill="none" stroke="var(--green)" stroke-width="3"/>
      <line x1="1110" y1="84" x2="1110" y2="541" stroke="var(--green)" stroke-width="2"/>
      <rect x="54" y="540" width="1085" height="8" fill="var(--gold)"/>
      <ellipse cx="600" cy="94" rx="132" ry="80" fill="var(--paper)"/>
    </svg>

    <div class="flourish flourish--left" role="img" aria-label="Ornamental corner flourish"></div>
    <div class="flourish flourish--right" role="img" aria-label="Ornamental corner flourish with trailing line"></div>

    <header class="brand">
      <span class="brand__name">Leafwell</span>
    </header>

    <h1 class="product-name">
      <span class="product-name__dot"></span>
      <span class="product-name__text">Moisturizer</span>
      <span class="product-name__dot"></span>
    </h1>

    <p class="description">All natural skin lotion infused with...<br>Lorem ipsum dolor sit amet, consectetur adip-<br>isicing elit, sed do eiusmod tempor incididunt<br>ut labore et dolore magna aliqua. Ut enim ad<br>minim veniam, quis nostrud exercitation</p>

    <section class="usage">
      <h2 class="usage__title">How to use:</h2>
      <p class="usage__text">Apply to skin in a circular ....Lorem ipsum dolor sit amet, consectetur adipisicing elit, sed do eiusmod tempor incididunt ut labore et dolore magna aliqua. Ut enim ad minim veniam, quis nostrud exercitation</p>
    </section>
  </main>
</body>
</html>
```